Book Cover design for Kindle and print book.

I’m looking for a unique and fresh approach for this book cover design because the content has a unique and fresh approach. For example I don't want a design that has steps, bulls eyes, targets or trophies. Because it incorporates some of the spiritual elements of VISION CRAFT I’d like it to encompass my signature purple colour #330066.

Think about people who want to set unrealistic or aspirational goals that will change the world - rather than people who want to achieve a simple goal.

I want a cover that will work for Kindle and for a print book, and, possibly later, a workbook.

NB My company logo is not intended to go onto the book, it's for your information only. However, an ISBN number will be included.

Target Market(s)

20-60 year old professional men and women who are motivated and want to achieve huge, aspirational goals while enjoying the journey.

Font styles to use
Serif
Sans Serif
Other font styles liked:
• I use Agenda in my manuals, but this isn't essential.

Requirements
Must have
• I prefer rounded shapes rather than sharp angles - but I'm pretty open to new designs. I also prefer font to be set in a combination of upper and lower case letters.
Nice to have
• purple colour #330066 if possible. I don't expect this to be all over the cover. Taking a quick look at my website http://lanternquay.example.nz might help. Otherwise I'm open to colour, but not a fan of green.
• I like the cleverness and simplicity of Born to Linger, (http://www.pelicanreads.example/Born-Linger-Thrive-Rivals-released/dp/Q77K42WX19/ref=sr_1_4?s=books&ie=UTF8&qid=1458845324&sr=1-4&keywords=Born+to+Linger) In fact all the book covers of Rolf and Ivan Marsh's books are impressive.
Should not have
• Bulls eyes, steps, targets or other symbols traditionally associated with VISION CRAFT.

```html
<!DOCTYPE html>
<html lang="en">
<head>
<meta charset="utf-8">
<title>Vision Craft – Book Cover</title>
<link rel="stylesheet" href="https://fonts.googleapis.com/css2?family=Cinzel:wght@400;500;600&family=Cabin:wght@400;500;600;700&display=swap">
<style>
  :root {
    --sky-light: #ffffff;
    --sky-mist: #e4f2f0;
    --sky-teal: #9ccbc7;
    --sky-deep: #5b9898;
    --sky-shadow: #2c5a5d;
    --title-orange: #e8601e;
    --title-amber: #f08a2c;
    --ink-purple: #330066;
    --author-white: #ffffff;
    --sun-core: #fff6d8;
    --sun-gold: #f7b53a;
    --sun-orange: #ef7d1c;
    --sun-rim: #e0561a;
  }

  html, body {
    margin: 0;
    padding: 0;
    width: 790px;
    height: 1200px;
    overflow: hidden;
    background: var(--sky-shadow);
  }

  .cover {
    position: relative;
    width: 790px;
    height: 1200px;
    overflow: hidden;
    background:
      radial-gradient(ellipse 560px 600px at 395px 520px, var(--sky-light) 0%, rgba(255,255,255,0.85) 35%, rgba(228,242,240,0) 78%),
      radial-gradient(ellipse 760px 960px at 395px 560px, var(--sky-mist) 0%, var(--sky-teal) 58%, var(--sky-deep) 90%),
      var(--sky-deep);
  }

  .cover::after {
    content: "";
    position: absolute;
    left: 0; right: 0; bottom: 0;
    height: 280px;
    background: linear-gradient(to bottom, rgba(44,90,93,0) 0%, rgba(44,90,93,0.5) 60%, rgba(34,74,78,0.75) 100%);
    pointer-events: none;
  }

  .title,
  .subtitle,
  .sun-disc,
  .tagline,
  .author {
    position: absolute;
    z-index: 1;
  }

  .title {
    top: 100px;
    left: 0;
    width: 100%;
    margin: 0;
    text-align: center;
    font-family: "Cinzel", serif;
    font-weight: 500;
    font-size: 94px;
    letter-spacing: 1px;
    line-height: 1;
    color: var(--title-orange);
    background: linear-gradient(to bottom, var(--title-amber), var(--title-orange) 60%, #d9501a);
    -webkit-background-clip: text;
    background-clip: text;
    -webkit-text-fill-color: transparent;
  }

  .subtitle {
    top: 208px;
    left: 0;
    width: 100%;
    margin: 0;
    text-align: center;
    font-family: "Cabin", sans-serif;
    font-weight: 400;
    font-size: 42px;
    line-height: 50px;
    color: var(--ink-purple);
  }

  .sun-disc {
    left: 156px;
    top: 355px;
    width: 478px;
    height: 488px;
  }

  .tagline {
    top: 924px;
    left: 0;
    width: 100%;
    margin: 0;
    text-align: center;
    font-family: "Cabin", sans-serif;
    font-weight: 400;
    font-size: 31px;
    line-height: 38px;
    color: var(--ink-purple);
  }

  .tagline .method-name {
    font-size: 42px;
    font-weight: 500;
    letter-spacing: 0.5px;
  }

  .author {
    top: 1110px;
    left: 0;
    width: 100%;
    margin: 0;
    text-align: center;
    font-family: "Cabin", sans-serif;
    font-weight: 700;
    font-size: 40px;
    line-height: 50px;
    color: var(--author-white);
  }
</style>
</head>
<body>
  <main class="cover">
    <h1 class="title">VISION CRAFT</h1>
    <p class="subtitle">7 Practices to Realise<br>Meaningful Achievement</p>

    <svg class="sun-disc" viewBox="0 0 478 488" role="img" aria-label="Glowing golden-orange disc filled with an ornamental pattern of spirals radiating light from its centre">
      <defs>
        <radialGradient id="sunGlow" cx="50%" cy="45%" r="60%">
          <stop offset="0%" stop-color="var(--sun-core)"/>
          <stop offset="22%" stop-color="#fde3a0"/>
          <stop offset="50%" stop-color="var(--sun-gold)"/>
          <stop offset="80%" stop-color="var(--sun-orange)"/>
          <stop offset="100%" stop-color="var(--sun-rim)"/>
        </radialGradient>
      </defs>
      <ellipse cx="239" cy="244" rx="238" ry="243" fill="url(#sunGlow)"/>
    </svg>

    <p class="tagline">Using the <span class="method-name">R.A.D.I.A.N.T.</span> strategy<br>to shape your future.</p>

    <p class="author">Harriet Vellan</p>
  </main>
</body>
</html>
```